Lume Hart Co Need a custom graphic

I need to have the attached chart re-designed in a hand colored pencil format. The heading needs to be changed to "The most effective methods for hiring sales people". Do not include the background logo in the sample file.

Place the attached Lume Hart Co logo next to the most effective methods (91%)

```html
<!DOCTYPE html>
<html lang="en">
<head>
<meta charset="utf-8">
<title>The Most Effective Methods for Hiring Sales People</title>
<link rel="stylesheet" href="https://fonts.googleapis.com/css2?family=Kalam:wght@700&display=swap">
<style>
  :root {
    --sky: #1a8fd8;
    --sky-soft: #5fb4e8;
    --navy: #1b2a5c;
    --grid: #d9d9d9;
    --paper: #ffffff;
  }
  html, body {
    margin: 0;
    padding: 0;
    width: 1200px;
    height: 807px;
    overflow: hidden;
    background: var(--paper);
  }
  .chart {
    display: block;
    width: 1200px;
    height: 807px;
  }
  .title-band { fill: var(--sky); }
  .title-band-edge { fill: none; stroke: var(--sky-soft); stroke-width: 3; }
  .chart-title {
    font-family: "Kalam", cursive;
    font-weight: 700;
    font-size: 32px;
    fill: var(--paper);
    letter-spacing: 1px;
  }
  .grid-line {
    stroke: var(--grid);
    stroke-width: 1.2;
    stroke-dasharray: 7 6;
  }
  .tick-label {
    font-family: "Kalam", cursive;
    font-weight: 700;
    font-size: 21px;
    fill: var(--navy);
  }
  .axis-title {
    font-family: "Kalam", cursive;
    font-weight: 700;
    font-size: 32px;
    fill: var(--sky);
    letter-spacing: 1.5px;
  }
  .trend-line {
    fill: none;
    stroke: var(--sky);
    stroke-width: 3;
    stroke-linejoin: round;
  }
  .data-point {
    fill: var(--sky);
    stroke: var(--navy);
    stroke-width: 1.6;
  }
  .point-label {
    font-family: "Kalam", cursive;
    font-weight: 700;
    font-size: 15px;
    fill: var(--navy);
  }
  .pointer {
    fill: none;
    stroke: var(--navy);
    stroke-width: 1.8;
    stroke-linecap: round;
    stroke-linejoin: round;
  }
  .brand-box { fill: var(--navy); }
  .brand-mark { fill: var(--sky); }
  .brand-name {
    font-family: "Kalam", cursive;
    font-weight: 700;
    font-size: 20px;
    fill: var(--paper);
  }
</style>
</head>
<body>
<svg class="chart" viewBox="0 0 1200 807" xmlns="http://www.w3.org/2000/svg">
  <defs>
    <marker id="arrowhead" viewBox="0 0 10 10" refX="8" refY="5" markerWidth="7" markerHeight="7" orient="auto-start-reverse">
      <path d="M1 1 L9 5 L1 9" fill="none" stroke="#1b2a5c" stroke-width="1.6" stroke-linecap="round"/>
    </marker>
  </defs>

  <!-- Title band -->
  <path class="title-band" d="M0 0 H1200 V62 L1170 66 L1130 61 L1080 68 L1020 62 L960 67 L900 61 L840 68 L780 62 L720 67 L660 61 L600 68 L540 62 L480 67 L420 61 L360 68 L300 62 L240 67 L180 61 L120 68 L60 62 L0 66 Z"/>
  <path class="title-band-edge" d="M0 70 L80 66 L160 71 L240 66 L320 71 L400 66 L480 71 L560 66 L640 71 L720 66 L800 71 L880 66 L960 71 L1040 66 L1120 71 L1200 66"/>
  <text class="chart-title" x="620" y="48" text-anchor="middle">THE MOST EFFECTIVE METHODS FOR HIRING SALES PEOPLE</text>

  <!-- Grid -->
  <g class="grid">
    <line class="grid-line" x1="124" y1="100" x2="1175" y2="100"/>
    <line class="grid-line" x1="124" y1="170" x2="1175" y2="170"/>
    <line class="grid-line" x1="124" y1="241" x2="1175" y2="241"/>
    <line class="grid-line" x1="124" y1="311" x2="1175" y2="311"/>
    <line class="grid-line" x1="124" y1="381" x2="1175" y2="381"/>
    <line class="grid-line" x1="124" y1="451" x2="1175" y2="451"/>
    <line class="grid-line" x1="124" y1="521" x2="1175" y2="521"/>
    <line class="grid-line" x1="124" y1="592" x2="1175" y2="592"/>
    <line class="grid-line" x1="124" y1="662" x2="1175" y2="662"/>
    <line class="grid-line" x1="124" y1="746" x2="1175" y2="746"/>
    <line class="grid-line" x1="124" y1="92" x2="124" y2="746"/>
    <line class="grid-line" x1="238" y1="92" x2="238" y2="746"/>
    <line class="grid-line" x1="353" y1="92" x2="353" y2="746"/>
    <line class="grid-line" x1="467" y1="92" x2="467" y2="746"/>
    <line class="grid-line" x1="582" y1="92" x2="582" y2="746"/>
    <line class="grid-line" x1="696" y1="92" x2="696" y2="746"/>
    <line class="grid-line" x1="810" y1="92" x2="810" y2="746"/>
    <line class="grid-line" x1="925" y1="92" x2="925" y2="746"/>
    <line class="grid-line" x1="1039" y1="92" x2="1039" y2="746"/>
    <line class="grid-line" x1="1154" y1="92" x2="1154" y2="746"/>
  </g>

  <!-- Y axis ticks -->
  <g class="y-ticks">
    <text class="tick-label" x="66" y="108">0.90</text>
    <text class="tick-label" x="66" y="178">0.80</text>
    <text class="tick-label" x="66" y="249">0.70</text>
    <text class="tick-label" x="66" y="319">0.60</text>
    <text class="tick-label" x="66" y="389">0.50</text>
    <text class="tick-label" x="66" y="459">0.40</text>
    <text class="tick-label" x="66" y="529">0.30</text>
    <text class="tick-label" x="66" y="600">0.20</text>
    <text class="tick-label" x="66" y="670">0.10</text>
    <text class="tick-label" x="66" y="740">0.00</text>
  </g>

  <!-- Axis titles -->
  <text class="axis-title" transform="translate(46 400) rotate(-90)" text-anchor="middle">PREDICTIVE VALIDITY</text>
  <text class="axis-title" x="625" y="793" text-anchor="middle">HIRING METHOD</text>

  <!-- Trend line -->
  <polyline class="trend-line" points="214,690 298,620 407,597 502,594 597,567 691,570 788,510 883,370 982,306 1077,211 1171,95"/>
  <g class="points">
    <circle class="data-point" cx="214" cy="690" r="6"/>
    <circle class="data-point" cx="298" cy="620" r="6"/>
    <circle class="data-point" cx="407" cy="597" r="6"/>
    <circle class="data-point" cx="502" cy="594" r="6"/>
    <circle class="data-point" cx="597" cy="567" r="6"/>
    <circle class="data-point" cx="691" cy="570" r="6"/>
    <circle class="data-point" cx="788" cy="510" r="6"/>
    <circle class="data-point" cx="883" cy="370" r="6"/>
    <circle class="data-point" cx="982" cy="306" r="6"/>
    <circle class="data-point" cx="1077" cy="211" r="6"/>
    <circle class="data-point" cx="1171" cy="95" r="6"/>
  </g>

  <!-- Point labels with pointers -->
  <g class="labels">
    <text class="point-label" x="259" y="729">CULTURE TEST, 13%</text>
    <path class="pointer" d="M251 713 L226 701" marker-end="url(#arrowhead)"/>

    <text class="point-label" x="246" y="620" text-anchor="end">RESUME, 18%</text>
    <path class="pointer" d="M253 615 L284 616" marker-end="url(#arrowhead)"/>

    <text class="point-label" x="205" y="553">BEHAVIOR/ PERSONALITY TEST, 20%</text>
    <path class="pointer" d="M382 565 L401 587" marker-end="url(#arrowhead)"/>

    <text class="point-label" x="404" y="656">TRADITIONAL INTERVIEW, 20%</text>
    <path class="pointer" d="M524 628 L506 607" marker-end="url(#arrowhead)"/>

    <text class="point-label" x="465" y="516">REFERENCE CHECK, 23%</text>
    <path class="pointer" d="M574 534 L591 554" marker-end="url(#arrowhead)"/>

    <text class="point-label" x="681" y="630">EMOTIONAL INTELLIGENCE, 23%</text>
    <path class="pointer" d="M716 608 L698 587" marker-end="url(#arrowhead)"/>

    <text class="point-label" x="817" y="554">SKILLS TEST, 33%</text>
    <path class="pointer" d="M812 544 L794 523" marker-end="url(#arrowhead)"/>

    <text class="point-label" x="834" y="362" text-anchor="end">GENERAL MENTAL ABILITY, 51%</text>
    <path class="pointer" d="M842 362 L871 369" marker-end="url(#arrowhead)"/>

    <text class="point-label" x="932" y="295" text-anchor="end">HIGHLY STRUCTURED INTERVIEW WITH SCORECARD, 57%</text>
    <path class="pointer" d="M939 298 L966 306" marker-end="url(#arrowhead)"/>

    <text class="point-label" x="1018" y="217" text-anchor="end">MULTI-MEASUREMENT ASSESSMENT, 71%</text>
    <path class="pointer" d="M1028 212 L1062 212" marker-end="url(#arrowhead)"/>

    <text class="point-label" x="936" y="117" text-anchor="end">SALES-SPECIFIC MULTI-MEASUREMENT ASSESSMENT, 91%</text>
    <path class="pointer" d="M1129 104 L1157 96" marker-end="url(#arrowhead)"/>
  </g>

  <!-- Brand tag -->
  <g class="brand">
    <rect class="brand-box" x="946" y="85" width="176" height="46" rx="6"/>
    <rect class="brand-mark" x="958" y="101" width="13" height="13"/>
    <text class="brand-name" x="980" y="115">Lume Hart Co</text>
  </g>
</svg>
</body>
</html>
```